NEW Modern Sleek Business Card for VR Language Startup

Our startup is using VR to lead the next wave of world language education. We need a two-sided business card that introduces the larger organization (Quorvel Language Inc) and our contact info on one side and shows the product, Lumidrasca, on the other side.

Side 1 (contact info)= Quorvel Logo and Contact info (name, title, phone, email)

Side 2 (product)= Lumidrasc logo, text, and website
Text= Culturally Immersive Language Learning Games
Website= www.lumidrasc.example

Target Market(s)

Education, Technology

Contact Information for Business Card

Contact info will be updated upon approval of the design. For now, put this as a placeholder.

Perry Hollins
Founder & CEO
phollins@mailtrove.example
(555)-014-2736

Font styles to use
Other font styles liked:
• Gibson and Century Gothic are the brand fonts

Requirements
Nice to have
• I would love to see cohesion between the design and colors of the two logos. I have attached a few business card designs that I like, so you can get a feel for my preferred style.

```html
<!DOCTYPE html>
<html lang="en">
<head>
<meta charset="utf-8">
<title>Lumidrasc &amp; Quorvel Language — Business Card</title>
<link href="https://fonts.googleapis.com/css2?family=Questrial&display=swap" rel="stylesheet">
<style>
  :root {
    --navy: #27334a;
    --white: #ffffff;
    --sky: #3fb6e8;
    --violet: #6b6fb8;
    --ink: #555a60;
    --ink-soft: #6a6e73;
    --edge: #d6d8dc;
    --shadow: #e2e3e5;
  }
  * { margin: 0; padding: 0; box-sizing: border-box; }
  html, body {
    width: 1200px; height: 1000px; overflow: hidden;
    background: var(--white);
    font-family: "Questrial", "Century Gothic", sans-serif;
  }
  .canvas { position: relative; width: 1200px; height: 1000px; }

  .card { position: absolute; left: 293px; width: 513px; height: 294px; overflow: hidden; }
  .card-shadow {
    position: absolute; left: 293px; width: 513px; height: 10px;
    background: radial-gradient(ellipse at 50% 0%, var(--shadow) 0%, rgba(226,227,229,0) 70%);
  }

  /* Product side */
  .card--product { top: 175px; background: var(--navy); }
  .card--product .circuit-strip {
    position: absolute; left: 8px; top: 0; width: 76px; height: 294px;
    background: linear-gradient(90deg, rgba(107,111,184,0.35), rgba(63,182,232,0.35));
  }
  .product-mark {
    position: absolute; right: 38px; top: 84px;
    display: flex; align-items: center; gap: 8px;
    color: var(--white); font-size: 19px; letter-spacing: 0.2px;
  }
  .product-mark .dot { width: 12px; height: 12px; border-radius: 50%; background: var(--sky); }
  .tagline {
    position: absolute; left: 108px; top: 162px;
    color: var(--white); font-size: 22.5px; line-height: 28.5px;
    text-transform: uppercase; letter-spacing: 0.2px;
  }
  .website {
    position: absolute; left: 107px; top: 250px;
    color: var(--sky); font-size: 16px;
  }

  /* Contact side */
  .card--contact { top: 534px; background: var(--white); border: 1px solid var(--edge); }
  .circuit-band {
    position: absolute; left: 0; top: 4px; width: 100%; height: 72px;
    background: linear-gradient(180deg, rgba(63,182,232,0.18), rgba(107,111,184,0.22));
  }
  .company-mark {
    position: absolute; left: 46px; top: 190px; width: 150px;
    display: flex; flex-direction: column; align-items: center; gap: 10px;
    color: var(--ink); font-size: 18px; letter-spacing: 2px; text-transform: uppercase;
    text-align: center; line-height: 22px;
  }
  .company-mark .dot { width: 14px; height: 14px; border-radius: 50%; background: var(--sky); }
  .person { position: absolute; right: 47px; top: 112px; text-align: right; }
  .person-name { color: var(--ink); font-size: 37px; line-height: 40px; }
  .person-title { color: var(--sky); font-size: 16px; letter-spacing: 0.3px; margin-top: 2px; }
  .contact-list { position: absolute; left: 273px; top: 202px; list-style: none; }
  .contact-list li {
    display: flex; align-items: center; gap: 8px;
    color: var(--ink-soft); font-size: 13px; height: 22px;
  }
  .contact-list svg { width: 17px; height: 17px; flex: none; }
</style>
</head>
<body>
<main class="canvas">

  <section class="card card--product">
    <div class="circuit-strip" role="img" aria-label="Vertical circuit-trace pattern in blue and violet"></div>
    <div class="product-mark"><span class="dot"></span><span>Lumidrasc</span></div>
    <p class="tagline">Culturally immersive<br>language learning<br>games</p>
    <p class="website">www.lumidrasc.example</p>
  </section>
  <div class="card-shadow" style="top:469px"></div>

  <section class="card card--contact">
    <div class="circuit-band" role="img" aria-label="Horizontal circuit-trace pattern in light blue and violet"></div>
    <div class="company-mark"><span class="dot"></span><span>Quorvel<br>Language</span></div>
    <div class="person">
      <h1 class="person-name">Perry Hollins</h1>
      <p class="person-title">FOUNDER &amp; CEO</p>
    </div>
    <ul class="contact-list">
      <li>
        <svg viewBox="0 0 18 18" aria-hidden="true"><circle cx="9" cy="9" r="9" fill="#3fb6e8"/><rect x="4.5" y="6" width="9" height="6.5" rx="0.8" fill="#fff"/><path d="M4.8 6.4 9 9.6l4.2-3.2" stroke="#3fb6e8" stroke-width="1" fill="none"/></svg>
        phollins@mailtrove.example
      </li>
      <li>
        <svg viewBox="0 0 18 18" aria-hidden="true"><circle cx="9" cy="9" r="9" fill="#3fb6e8"/><path d="M6.2 4.6c.5-.3 1 0 1.2.4l.8 1.6c.2.4.1.8-.2 1.1l-.6.5c.5 1.1 1.3 1.9 2.4 2.4l.5-.6c.3-.3.7-.4 1.1-.2l1.6.8c.4.2.7.7.4 1.2-.5.9-1.4 1.4-2.3 1.2-3-.7-5.3-3-6-6-.2-.9.3-1.8 1.1-2.4z" fill="#fff"/></svg>
        (555)-014-2736
      </li>
    </ul>
  </section>
  <div class="card-shadow" style="top:828px"></div>

</main>
</body>
</html>
```